Create a packaging design for coffee pouches

We specialize in roasting speciality coffee and are selling it to our customers in 250g bags. We usually have around 8-10 different coffee origins and we change them every 6 months or so. The labels need to be 120mm tall and 70mm wide. Because we change origins so often we need the main label (120x70) to contain a blank square (around 40mm wide with 20mm height) on witch we can stick the second part of the label. This second label must be either Illustrator or Photoshop file that we can easily change the text to, so that every time we change the coffee origins we just print out these small labels and use on the main label. The main label must also be illustratior or photoshop file and must contain the following details: Our company's logo, the small label space for the coffee origins, Roast date (data prajirii in romanian) with a blank space (aprox 30mm x 5mm) where we can write the date itself, Type of roasting (Prajita in romanian) with 3 different roast styles (light, medium, dark) that have boxes that we can tick, and the weight of the bag, e.g. 250g (with the international weight icon). Design wise we like to keep it simple but unconventional. Check out our FB page found our website [login to view URL] to get an idea of our marketing image. I have attached our logo to this project and our current label that we use and are not pleased at all with. You can change the layout as much as you like, if you have a better vision than us we will welcome it!

```html
<!DOCTYPE html>
<html lang="ro">
<head>
<meta charset="utf-8">
<title>Ardeal Roastery – El Salvador coffee pouch</title>
<link rel="stylesheet" href="https://fonts.googleapis.com/css2?family=Cinzel:wght@400;700&display=swap">
<style>
  :root {
    --page: #d9d9d9;
    --pouch: #0b0b0b;
    --gold: #a8763a;
    --gold-dark: #6e4a1f;
    --gold-light: #b98845;
    --paper: #ffffff;
    --muted: #9a9a9a;
    --roast-dark: #5a3217;
  }
  * { margin: 0; padding: 0; box-sizing: border-box; }
  html, body {
    width: 947px; height: 1200px; overflow: hidden;
    background: var(--page);
    font-family: "Cinzel", serif;
  }
  .canvas { position: relative; width: 947px; height: 1200px; }
  .pouch {
    position: absolute; left: 212px; top: 160px;
    width: 528px; height: 870px;
    background: var(--pouch);
    border-radius: 14px 14px 6px 6px;
  }
  .pattern-band {
    position: absolute; top: 140px; width: 74px; height: 582px;
    background: linear-gradient(180deg, var(--gold-light), var(--gold-dark) 55%, var(--gold) 100%);
    opacity: .85;
  }
  .pattern-band--left { left: 62px; }
  .pattern-band--right { right: 62px; }
  .brand {
    position: absolute; left: 0; right: 0; top: 200px;
    display: flex; align-items: center; justify-content: center; gap: 10px;
  }
  .brand-dot {
    width: 14px; height: 14px; border-radius: 50%; background: var(--gold);
  }
  .brand-name {
    font-size: 22px; font-weight: 400; color: var(--gold); letter-spacing: 2px;
  }
  .ornament {
    position: absolute; left: 190px; top: 358px; width: 148px; height: 26px;
    background: linear-gradient(90deg, transparent, var(--gold) 25%, var(--gold) 75%, transparent);
    border-radius: 13px;
  }
  .origin {
    position: absolute; left: 0; right: 0; top: 400px;
    text-align: center; color: var(--gold); line-height: 1; font-weight: 400;
  }
  .origin__country, .origin__farm { display: block; font-size: 40px; margin-bottom: 4px; }
  .origin__name { display: block; font-size: 68px; margin-top: 2px; }
  .roast-date {
    position: absolute; left: 0; right: 0; top: 612px; text-align: center;
  }
  .roast-date__label { font-size: 14px; color: var(--muted); letter-spacing: 1px; }
  .roast-date__field {
    margin: 8px auto 0; width: 196px; height: 26px;
    background: var(--paper); border: 1px solid var(--gold);
    color: var(--gold-dark); font-size: 18px; line-height: 24px;
  }
  .roast-type {
    position: absolute; left: 0; right: 0; top: 692px; text-align: center;
  }
  .roast-type__title { font-size: 24px; color: var(--gold-light); letter-spacing: 1px; font-weight: 400; }
  .roast-options {
    list-style: none; display: flex; justify-content: center; gap: 22px;
    margin-top: 18px;
  }
  .roast-option { display: flex; align-items: center; gap: 6px; font-size: 19px; }
  .roast-option svg { width: 30px; height: 30px; }
  .roast-option--light { color: var(--paper); }
  .roast-option--medium { color: var(--gold); }
  .roast-option--dark { color: var(--roast-dark); }
  .net-weight {
    position: absolute; left: 203px; top: 805px;
    width: 123px; height: 36px; border-radius: 12px 12px 4px 4px;
    background: var(--gold);
    color: var(--paper); font-size: 20px; text-align: center; line-height: 36px;
    font-family: Arial, sans-serif;
  }
</style>
</head>
<body>
<div class="canvas">
  <div class="pouch">
    <div class="pattern-band pattern-band--left" role="img" aria-label="Brown damask pattern band"></div>
    <div class="pattern-band pattern-band--right" role="img" aria-label="Brown damask pattern band"></div>

    <div class="brand">
      <span class="brand-dot"></span>
      <span class="brand-name">Ardeal Roastery</span>
    </div>

    <div class="ornament" role="img" aria-label="Gold flourish ornament with small crown"></div>

    <h1 class="origin">
      <span class="origin__country">El Salvador</span>
      <span class="origin__farm">Finca de la</span>
      <span class="origin__name">Brisa</span>
    </h1>

    <div class="roast-date">
      <p class="roast-date__label">Data Prăjirii</p>
      <div class="roast-date__field">__ / __ / 20__</div>
    </div>

    <div class="roast-type">
      <p class="roast-type__title">Prăjită</p>
      <ul class="roast-options">
        <li class="roast-option roast-option--light">
          <svg viewBox="0 0 30 30"><circle cx="15" cy="15" r="13" fill="#fff" stroke="#000" stroke-width="2"/><circle cx="15" cy="15" r="9" fill="none" stroke="#000" stroke-width="1.5"/></svg>Light
        </li>
        <li class="roast-option roast-option--medium">
          <svg viewBox="0 0 30 30"><circle cx="15" cy="15" r="13" fill="#8c6230" stroke="#fff" stroke-width="2"/><circle cx="15" cy="15" r="9" fill="none" stroke="#fff" stroke-width="1.5"/></svg>Medium
        </li>
        <li class="roast-option roast-option--dark">
          <svg viewBox="0 0 30 30"><circle cx="15" cy="15" r="13" fill="#5a3217" stroke="#fff" stroke-width="2"/><circle cx="15" cy="15" r="9" fill="none" stroke="#fff" stroke-width="1.5"/></svg>Dark
        </li>
      </ul>
    </div>

    <div class="net-weight">℮ 250 g.</div>
  </div>
</div>
</body>
</html>
```